RISE with Abbot Leng Book Cover

We need a Book cover for a Spiritual Book entitled:

R.I.S.E. with Abbot Leng: Reflective Inner Study Exercises with a Present Era Hermit Sage

By Ven. Abbot Leng Odile Rask, MPH

By 2x No. 1 Best Selling Author

See sketch: By 2x No. 1 Best Selling Author in WHITE Text
The tape where above is written and 1 in red Text

ABBOT LENG ODILE RASK, MPH (White and Thick BOLD TEXT - see attachment KE Baltor)

R.I.S.E. ABBOT LENG (Use the Wayfinder FONT and style in WHITE text/colour)

with (use the Corinne Haldwell book - No. 1 Best Seller Text Style in white or red)

Reflective Inner Study Exercises with a Present Era Hermit Sage (Use Harwick book - red block at the bottom)

Please clean up the picture as it is a raw file and take out the shadow on Abbot Leng's face. Make us more translucent and light filled. Clean up the face and crop to look like the sketch (cro just underneath the white cuff on Monk's sleeve). Keep to of pic as it to use the right hand space for By No. 1 Best Selling Author and No. 1 text and red band.

```html
<!DOCTYPE html>
<html lang="en">
<head>
<meta charset="utf-8">
<title>R.I.S.E. with Abbot Leng — Book Cover</title>
<link rel="stylesheet" href="https://fonts.googleapis.com/css2?family=Oswald:wght@500;700&family=Montserrat:wght@700;800;900&display=swap">
<style>
  :root {
    --navy: #13213f;
    --navy-deep: #0c1730;
    --white: #ffffff;
    --orange: #f2a51c;
    --gold: #f6c21a;
    --yellow: #f3e51f;
    --red: #c8202a;
    --red-band: #d0262d;
  }
  * { margin: 0; padding: 0; box-sizing: border-box; }
  html, body { width: 798px; height: 1200px; overflow: hidden; background: var(--navy-deep); }
  .cover {
    position: relative;
    width: 798px;
    height: 1200px;
    overflow: hidden;
    font-family: "Montserrat", Arial, sans-serif;
    color: var(--white);
  }
  .cover-photo {
    position: absolute; inset: 0;
    background:
      radial-gradient(ellipse at 25% 12%, #b9c4a0 0%, rgba(185,196,160,0) 40%),
      radial-gradient(ellipse at 60% 28%, #d6b39a 0%, rgba(214,179,154,0) 30%),
      radial-gradient(ellipse at 22% 30%, #c9a58c 0%, rgba(201,165,140,0) 25%),
      linear-gradient(180deg, #6f7d5a 0%, #39402f 28%, #1c2338 50%, #14203f 75%, #0f1a33 100%);
  }
  .corner-ribbon { position: absolute; top: 0; right: 0; width: 798px; height: 340px; }
  .author-block {
    position: absolute; left: 458px; top: 438px;
    font-family: "Oswald", Impact, sans-serif; font-weight: 700;
    text-transform: uppercase; line-height: 1; text-shadow: 0 2px 4px rgba(0,0,0,.35);
  }
  .author-title { font-size: 30px; letter-spacing: .5px; }
  .author-name { font-size: 45px; margin-top: 6px; letter-spacing: .5px; }
  .author-degree { font-size: 54px; margin-top: 4px; }
  .series-mark {
    position: absolute; left: 48px; top: 490px;
    display: flex; align-items: center; gap: 10px;
  }
  .series-mark-dot { width: 12px; height: 12px; border-radius: 50%; background: var(--orange); }
  .series-mark-name {
    font-family: "Oswald", Impact, sans-serif; font-weight: 700;
    font-size: 28px; letter-spacing: .3px; line-height: 1; color: var(--white);
    text-shadow: 0 2px 4px rgba(0,0,0,.35);
  }
  .tagline-box {
    position: absolute; left: 190px; top: 636px; width: 402px; height: 84px;
    background: var(--red-band);
    display: flex; flex-direction: column; align-items: center; justify-content: center;
    font-weight: 800; font-size: 15.5px; letter-spacing: 1.3px; line-height: 1.35;
    text-transform: uppercase; text-align: center;
  }
  .title { position: absolute; left: 0; right: 0; top: 738px; text-align: center; }
  .title-acronym {
    display: block;
    font-weight: 900; font-size: 124px; line-height: 1; letter-spacing: 2px;
    text-shadow: 0 3px 6px rgba(0,0,0,.3);
  }
  .title-with {
    display: flex; align-items: center; justify-content: center; gap: 12px;
    margin-top: 4px; color: var(--gold); font-weight: 900; font-size: 50px; line-height: 1;
  }
  .title-with::before, .title-with::after { content: ""; width: 58px; height: 6px; background: var(--gold); }
  .title-name {
    display: block;
    font-weight: 900; font-size: 96px; line-height: 1; margin-top: 6px; letter-spacing: 1px;
    text-shadow: 0 3px 6px rgba(0,0,0,.3);
  }
  .subtitle {
    position: absolute; left: 0; right: 0; top: 1035px; text-align: center;
    color: var(--yellow); font-weight: 700; font-size: 27px; line-height: 1.2;
  }
  .subtitle-emphasis { color: var(--gold); font-weight: 800; font-size: 35px; display: block; margin-top: 2px; }
</style>
</head>
<body>
<main class="cover">
  <div class="cover-photo" role="img" aria-label="Photo of Abbot Leng, a shaven-headed monk in a dark robe, smiling and cupping the chin of a laughing companion in a white-collared dark robe, in front of blurred green foliage"></div>

  <svg class="corner-ribbon" viewBox="0 0 798 340">
    <polygon points="480,0 798,0 798,318" fill="#c8202a"/>
    <polygon points="565,0 690,0 798,108 798,233" fill="#f2a51c"/>
    <text x="752" y="56" fill="#ffffff" font-family="Montserrat, Arial, sans-serif" font-weight="900" font-size="40" text-anchor="middle">#1</text>
    <g transform="translate(700,72) rotate(45)" font-family="Montserrat, Arial, sans-serif" font-weight="900" fill="#c8202a" text-anchor="middle" font-size="22">
      <text x="0" y="-8">2X NO. 1 BEST</text>
      <text x="0" y="19">SELLING AUTHOR</text>
    </g>
    <text transform="translate(654,132) rotate(45)" x="0" y="5" fill="#ffffff" font-family="Montserrat, Arial, sans-serif" font-weight="700" font-size="13.5" text-anchor="middle">By Ven. Abbot Leng Odile Rask, MPH</text>
  </svg>

  <div class="series-mark">
    <span class="series-mark-dot"></span>
    <span class="series-mark-name">R.I.S.E. ABBOT LENG</span>
  </div>

  <div class="author-block">
    <div class="author-title">Abbot</div>
    <div class="author-name">Leng Odile Rask,</div>
    <div class="author-degree">MPH</div>
  </div>

  <div class="tagline-box">
    <span>Reflective Inner Study Exercises</span>
    <span>with a Present Era Hermit Sage</span>
  </div>

  <h1 class="title">
    <span class="title-acronym">R.I.S.E</span>
    <span class="title-with">WITH</span>
    <span class="title-name">ABBOT LENG</span>
  </h1>

  <p class="subtitle">
    Reflective Inner Study Exercises with<br>
    a Present Era
    <span class="subtitle-emphasis">Hermit Sage</span>
  </p>
</main>
</body>
</html>
```